Educational Flashcard Packaging Box Design

We are an educational resource provider in Australia. We have a new product launching for high school students, age 13-18. Thye are flashcards that help students with literacy. We need the box design that will store the cards when the students keep them in the bag at school. They need to be fun and colourful.
Our brand colours are
#06D8D8
#EF0081
#FFC904
#FF9900

The 36 flashcards all have a different colour to make up a rainbow. See the image of the flashcards attached.

The box template is uploaded in the files.
The box dimensions are 91 x 35 x 129mm.
Updates

I had a baby on the 2nd June and am in the hospital until the 8th June so I haven't been able to manage the project.

Target Market(s)

School students age 12 -18

Requirements
Must have
• Name of the product: Brightmark Mastery Flashcards
Fun and engaging design.
Bright colours.
Our logo - attached.
Text:
Get results you can be proud of.
36 flashcards + instructions
Increase key word knowledge and understanding.
(C) Harbourline Study Guild 2021
Wattlebrook, Australia.
hsguild.edu.au
Nice to have
• Instructions for the back of the box:
1. Box the key word in every question and check its meaning in the flashcards.
2. Write the meaning above the key word.
3. Use the key word metalanguage in your answer, e.g. describe; use the words characteristics and features in your answer. E.g. explain; use the words cause and effect in your answer and use linking words to demonstrate the relationships.
4. Be sure to add relevant example/s where possible

```html
<!DOCTYPE html>
<html lang="en">
<head>
<meta charset="utf-8">
<title>Brightmark Mastery Flashcards – Box Dieline</title>
<link rel="stylesheet" href="https://fonts.googleapis.com/css2?family=Montserrat:wght@600;800;900&family=Open+Sans:wght@400;600;700&display=swap">
<style>
  :root {
    --teal: #06D8D8;
    --pink: #EF0081;
    --yellow: #FFC904;
    --orange: #FF9900;
    --white: #FFFFFF;
    --ink: #1B2A5C;
    --page: #FFFFFF;
    --cut: #9AA3AE;
  }
  html, body {
    margin: 0;
    padding: 0;
    background: var(--page);
    overflow: hidden;
  }
  .canvas {
    width: 1200px;
    height: 488px;
    overflow: hidden;
    position: relative;
    background: var(--page);
  }
  .dieline { display: block; }
  .fill-teal { fill: var(--teal); }
  .fill-pink { fill: var(--pink); }
  .fill-yellow { fill: var(--yellow); }
  .fill-orange { fill: var(--orange); }
  .fill-white { fill: var(--white); }
  .cut-edge { fill: none; stroke: var(--cut); stroke-width: 0.8; }
  .title {
    font-family: "Montserrat", sans-serif;
    font-weight: 900;
    fill: var(--ink);
  }
  .brand {
    font-family: "Montserrat", sans-serif;
    font-weight: 800;
    fill: var(--ink);
  }
  .body-copy {
    font-family: "Open Sans", sans-serif;
    font-weight: 600;
    fill: var(--ink);
  }
  .heading-copy {
    font-family: "Montserrat", sans-serif;
    font-weight: 800;
    fill: var(--ink);
  }
  .small-print {
    font-family: "Open Sans", sans-serif;
    font-weight: 400;
    fill: var(--ink);
  }
</style>
</head>
<body>
<main class="canvas">
  <svg class="dieline" width="1200" height="488" viewBox="0 0 1200 488" xmlns="http://www.w3.org/2000/svg">
    <defs>
      <linearGradient id="rainbow-cards" x1="0" y1="0" x2="1" y2="0">
        <stop offset="0" stop-color="#E8263A"/>
        <stop offset="0.2" stop-color="#FF9900"/>
        <stop offset="0.4" stop-color="#FFE03A"/>
        <stop offset="0.6" stop-color="#3CC463"/>
        <stop offset="0.8" stop-color="#2A8BE0"/>
        <stop offset="1" stop-color="#8A3FC7"/>
      </linearGradient>
      <symbol id="panel-background" viewBox="0 0 182 258" width="182" height="258">
        <rect class="fill-pink" width="182" height="258"/>
        <path class="fill-teal" d="M0 0 H182 V60 C150 75 120 40 80 50 C50 58 30 40 0 45 Z"/>
        <path class="fill-yellow" d="M182 40 C150 60 140 110 150 150 C160 190 120 215 60 222 C30 226 10 240 0 258 H182 Z"/>
        <path class="fill-white" d="M30 70 C60 45 120 55 150 70 C170 85 150 110 140 140 C130 175 110 195 70 200 C35 205 20 180 25 150 C30 120 5 95 30 70 Z"/>
      </symbol>
    </defs>

    <!-- glue flap -->
    <path class="fill-pink" d="M363 115 L337 128 L337 360 L363 373 Z"/>
    <path class="cut-edge" d="M363 115 L337 128 L337 360 L363 373"/>

    <!-- top tuck flap above back panel -->
    <path class="fill-teal" d="M363 115 V58 Q363 38 383 38 H525 Q545 38 545 58 V115 Z"/>
    <text class="title" font-size="13" text-anchor="middle" transform="translate(454 74) rotate(180)">
      <tspan x="0" y="0">Brightmark Mastery</tspan>
      <tspan x="0" y="15">Flashcards</tspan>
    </text>

    <!-- top dust flaps -->
    <path class="fill-pink" d="M545 115 L552 82 Q554 76 560 76 H608 L615 115 Z"/>
    <path class="fill-yellow" d="M797 115 L804 82 Q806 76 812 76 H860 L867 115 Z"/>

    <!-- back panel -->
    <g class="panel-back" transform="translate(363 115)">
      <use href="#panel-background" x="0" y="0" width="182" height="258"/>
      <rect x="108" y="10" width="64" height="34" rx="3" fill="url(#rainbow-cards)" role="img" aria-label="Fan of rainbow-coloured flashcards"/>
      <text class="heading-copy" x="38" y="80" font-size="9">Instructions</text>
      <text class="small-print" font-size="5.3">
        <tspan x="38" y="92">1. Box the key word in every question</tspan>
        <tspan x="38" y="99">and check its meaning in the flashcards.</tspan>
        <tspan x="38" y="108">2. Write the meaning above the key word.</tspan>
        <tspan x="38" y="117">3. Use the key word metalanguage in</tspan>
        <tspan x="38" y="124">your answer, e.g. describe; use the</tspan>
        <tspan x="38" y="131">words characteristics and features.</tspan>
        <tspan x="38" y="138">E.g. explain; use cause and effect</tspan>
        <tspan x="38" y="145">and linking words for relationships.</tspan>
        <tspan x="38" y="154">4. Be sure to add relevant example/s</tspan>
        <tspan x="38" y="161">where possible.</tspan>
      </text>
      <text class="body-copy" font-size="6.2">
        <tspan x="38" y="175">Get results you can</tspan>
        <tspan x="38" y="183">be proud of.</tspan>
      </text>
      <text class="small-print" font-size="5.6">
        <tspan x="16" y="232">© Harbourline Study Guild 2021</tspan>
        <tspan x="16" y="239">Wattlebrook, Australia.</tspan>
        <tspan x="16" y="246">hsguild.edu.au</tspan>
      </text>
    </g>

    <!-- pink side panel -->
    <g class="panel-side-left" transform="translate(545 115)">
      <rect class="fill-pink" width="70" height="258"/>
      <rect class="fill-teal" width="70" height="36"/>
      <rect class="fill-white" x="29" y="10" width="12" height="12"/>
      <text class="title" font-size="13" text-anchor="middle" transform="translate(35 140) rotate(90)">
        <tspan x="0" y="-4">Brightmark Mastery</tspan>
        <tspan x="0" y="12">Flashcards</tspan>
      </text>
    </g>

    <!-- front panel -->
    <g class="panel-front" transform="translate(615 115)">
      <use href="#panel-background" x="0" y="0" width="182" height="258"/>
      <rect class="fill-white" x="118" y="10" width="8" height="8"/>
      <text class="brand" x="130" y="17" font-size="6.5">Harbourline</text>
      <text class="brand" x="130" y="25" font-size="6.5">Study Guild</text>
      <rect x="48" y="70" width="86" height="52" rx="4" fill="url(#rainbow-cards)" role="img" aria-label="Fan of rainbow-coloured flashcards with a sample card"/>
      <text class="title" font-size="15" text-anchor="middle">
        <tspan x="88" y="146">Brightmark Mastery</tspan>
        <tspan x="88" y="165">Flashcards</tspan>
      </text>
      <text class="body-copy" font-size="6.2" text-anchor="middle">
        <tspan x="105" y="218">Increase key word knowledge</tspan>
        <tspan x="105" y="226">and understanding.</tspan>
      </text>
      <text class="heading-copy" x="105" y="242" font-size="8" text-anchor="middle">36 flashcards + instructions</text>
    </g>

    <!-- yellow side panel -->
    <g class="panel-side-right" transform="translate(797 115)">
      <rect class="fill-yellow" width="70" height="258"/>
      <rect class="fill-orange" y="222" width="70" height="36"/>
      <text class="title" font-size="13" text-anchor="middle" transform="translate(35 120) rotate(90)">
        <tspan x="0" y="-4">Brightmark Mastery</tspan>
        <tspan x="0" y="12">Flashcards</tspan>
      </text>
      <rect class="fill-white" x="29" y="236" width="12" height="12"/>
    </g>

    <!-- bottom tuck flap below front panel -->
    <path class="fill-yellow" d="M615 373 V430 Q615 450 635 450 H777 Q797 450 797 430 V373 Z"/>
    <text class="title" font-size="13" text-anchor="middle">
      <tspan x="706" y="402">Brightmark Mastery</tspan>
      <tspan x="706" y="417">Flashcards</tspan>
    </text>

    <!-- bottom dust flaps -->
    <path class="fill-pink" d="M545 373 L552 402 Q554 408 560 408 H608 L615 373 Z"/>
    <path class="fill-yellow" d="M797 373 L804 402 Q806 408 812 408 H860 L867 373 Z"/>

    <!-- panel outlines -->
    <rect class="cut-edge" x="363" y="115" width="504" height="258"/>
  </svg>
</main>
</body>
</html>
```